Veltrix Stationary

Design the stationary of Veltrix Promotions Group.

Veltrix is a BTL company, BTL meaning "below the line". In other words Veltrix is a Promotional Marketing company (the company that design the brands promotional activities).

The design should transmit creativity, agility, boldness.

I need:
* Bis Card
* Letter head
* Envelopes, both vertical and horizontal (for legal size), and letter envelope
* Folders
* PPT template (Title page and regular page)
* CD slip (CD envelope)
* ID card (employee card)

And what ever else you want to throw in.
Updates

Guys,

Something I missed from the brief.   The predominat color should be RED.

Also, have fun and play with the exclamation mark (!) of the logo. 

Hi guys, more comments:

Remember that Veltrix is a "creativity" agency, not in the advertising side but on the promotional side, and that should reflect on the stationary.

 I want a bold design.  Bold and yet crisp.

 

Guys, i just uploaded the Logo in AI format.

I Also uploaded the actual Veltrix Bis Card, wich I like.  So I will like to see some designs with that bis card approach.

Guys, I am so sorry, but I notice in your last post that I upladed a wrong design ("13154_marketing_group_veltrix_brief225630.ai").  The problem was that I asked the designer the file in AI format and he send me thw wrong file, and since I dont have Illustrator I could not verify it.

The differences are minor, I just already ask him the correct one (similar to the EPS file).

Sorry                                   

Just post the correct AI file : "Veltrix Logo.ai"

Reason: I'm expecting more designs to choose from and also I wont be available tomorrow to decide.

Reason: Sorry guys, but we are not there yet!

Target Market(s)

Marketing directors, Marketing Managers

Industry/Entity Type

Legal

Requirements
Must have
• Must work with the logo attached.
The predominat color should be RED.
Play and have fun with the exclamation mark (!).
Should not have
• * No old fonts

Should not be:
* boring
* Informal
* rigid

```html
<!DOCTYPE html>
<html lang="en">
<head>
<meta charset="utf-8">
<title>Veltrix Promotions Group — Business Card</title>
<link rel="stylesheet" href="https://fonts.googleapis.com/css2?family=Ubuntu:wght@700&family=Crimson+Pro:wght@400&family=Courier+Prime&family=Orbitron:wght@400&display=swap">
<style>
  :root {
    --canvas-bg: #e6e6e6;
    --ink-black: #111111;
    --card-black: #000000;
    --card-charcoal: #4a4a4c;
    --paper: #ffffff;
    --brand-red: #d0151c;
    --brand-red-deep: #c8141b;
    --brand-salmon: #ee8474;
    --text-grey: #6e6e6e;
    --text-grey-light: #9a9a9a;
  }
  html, body {
    margin: 0;
    padding: 0;
    width: 1200px;
    height: 1128px;
    overflow: hidden;
    background: var(--canvas-bg);
  }
  .canvas {
    position: relative;
    width: 1200px;
    height: 1128px;
  }
  .card {
    position: absolute;
    display: block;
  }
  .card--front { left: 52px; top: 73px; width: 742px; height: 424px; }
  .card--back  { left: 374px; top: 568px; width: 745px; height: 424px; }
  .brand-name {
    font-family: "Ubuntu", sans-serif;
    font-weight: 700;
    fill: var(--ink-black);
  }
  .person-name {
    font-family: "Crimson Pro", serif;
    fill: var(--text-grey);
  }
  .person-role {
    font-family: "Courier Prime", monospace;
    fill: var(--text-grey-light);
  }
  .contact-text {
    font-family: "Orbitron", sans-serif;
    fill: var(--paper);
  }
  .contact-icon {
    fill: none;
    stroke: var(--ink-black);
    stroke-width: 1.3;
  }
</style>
</head>
<body>
<main class="canvas">

  <!-- Front of card -->
  <svg class="card card--front" viewBox="0 0 526 300" aria-label="Business card front">
    <defs>
      <linearGradient id="front-fill" x1="0" y1="0" x2="1" y2="0">
        <stop offset="0" stop-color="var(--card-black)"/>
        <stop offset="1" stop-color="var(--card-charcoal)"/>
      </linearGradient>
    </defs>
    <rect class="card-base" width="526" height="300" fill="url(#front-fill)"/>
    <polygon class="name-band" points="90,105 520,36 526,186 116,255" fill="var(--paper)"/>
    <g class="identity" transform="rotate(-8 300 150)">
      <text class="brand-name" x="452" y="128" font-size="21" text-anchor="end">Veltrix Promotions Group</text>
      <circle class="brand-dot" cx="465" cy="121" r="6" fill="var(--brand-red)"/>
      <text class="person-name" x="214" y="186" font-size="21">Mara Delcourt</text>
      <text class="person-role" x="238" y="204" font-size="11">Designer</text>
    </g>
  </svg>

  <!-- Back of card -->
  <svg class="card card--back" viewBox="0 0 528 300" aria-label="Business card back">
    <defs>
      <linearGradient id="back-fill" x1="0" y1="0" x2="1" y2="0">
        <stop offset="0" stop-color="var(--brand-red-deep)"/>
        <stop offset="0.42" stop-color="var(--brand-red)"/>
        <stop offset="1" stop-color="var(--brand-salmon)"/>
      </linearGradient>
    </defs>
    <rect class="card-base" width="528" height="300" fill="url(#back-fill)"/>
    <polygon class="tab-shadow" points="34,10 52,4 82,246 62,238" fill="var(--ink-black)"/>
    <polygon class="logo-tab" points="38,0 217,0 255,219 80,247" fill="var(--paper)"/>
    <g class="identity" transform="translate(132 118) rotate(80.4)">
      <text class="brand-name" x="-8" y="5" font-size="15" text-anchor="middle">Veltrix Promotions Group</text>
      <circle class="brand-dot" cx="99" cy="0" r="5" fill="var(--brand-red)"/>
    </g>

    <g class="contacts" transform="rotate(-8 330 140)">
      <g class="contact contact--email">
        <rect class="contact-icon" x="212" y="104" width="20" height="13"/>
        <polyline class="contact-icon" points="212,104 222,112 232,104"/>
        <text class="contact-text" x="244" y="115" font-size="11.5">HELLO@VELTRIXPG.COM</text>
      </g>
      <g class="contact contact--web">
        <circle class="contact-icon" cx="222" cy="141" r="10"/>
        <ellipse class="contact-icon" cx="222" cy="141" rx="4.5" ry="10"/>
        <line class="contact-icon" x1="212" y1="141" x2="232" y2="141"/>
        <line class="contact-icon" x1="214" y1="135" x2="230" y2="135"/>
        <line class="contact-icon" x1="214" y1="147" x2="230" y2="147"/>
        <text class="contact-text" x="244" y="146" font-size="11.5">WWW.VELTRIXPG.COM</text>
      </g>
      <g class="contact contact--phone">
        <path class="contact-icon" d="M215,165 q-3,3 2,10 q6,8 11,6 l2,-3 l-5,-4 l-2,2 q-4,-2 -5,-6 l2,-2 l-3,-5 z"/>
        <text class="contact-text" x="244" y="178" font-size="11.5">(123) 456-789-000</text>
      </g>
    </g>
  </svg>

</main>
</body>
</html>
```